Kivora - a fintech company - business card

We need a business card design for our Payments Technology company in Sydney, Australia. We provide business with payment solutions expanding across EFTPOS machines, online payment gateways and mobile payment solutions. We would like to see designs that are clean, classy and professional.
Target Market(s)
Business professionals, executives, c-suite
Industry/Entity Type
Fintech
Contact Information for Business Card
Will be on 400gsm. Logo will most likely be spot gloss unless designer recommends otherwise.
Font styles to use
Sans Serif
Requirements
Must have
- We need our website (kivora.com.au), email (contact@kivora.com.au), mobile (0455 806 274) and direct phone number (02 7391 5082) to feature on the card along with our logo (attached) and the words "EFTPOS | ONLINE | MOBILE"
- Font = Roboto

```html
<!DOCTYPE html>
<html lang="en">
<head>
<meta charset="utf-8">
<title>Kivora – Business Card</title>
<link rel="stylesheet" href="https://fonts.googleapis.com/css2?family=Roboto:wght@400;500;700&family=Roboto+Condensed:wght@700&display=swap">
<style>
  :root {
    --bg: #e9e6e1;
    --blue-deep: #14609a;
    --blue-mid: #1f8dc2;
    --blue-brand: #1b7fbf;
    --teal: #49c6b8;
    --white: #ffffff;
    --paper: #eef0f3;
    --grey-brand: #6d7378;
    --ink: #1e2a33;
    --rule: #1f6fa6;
    --social: #b9c3cc;
  }
  * { margin: 0; padding: 0; box-sizing: border-box; }
  html, body { width: 1200px; height: 1023px; overflow: hidden; background: var(--bg); }
  .canvas { position: relative; width: 1200px; height: 1023px; }

  .card {
    position: absolute; left: 250px; width: 700px; height: 400px;
    border-radius: 22px; overflow: hidden;
    box-shadow: 0 10px 28px rgba(0,0,0,.18);
  }

  /* Front */
  .card-front {
    top: 70px;
    background: radial-gradient(ellipse at 45% 35%, var(--blue-mid) 0%, var(--blue-deep) 85%);
  }
  .front-lockup {
    position: absolute; left: 70px; top: 110px;
    display: flex; align-items: center; gap: 36px;
  }
  .front-mark { width: 170px; height: 170px; border-radius: 50%; background: var(--white); }
  .front-name {
    font-family: "Roboto Condensed", sans-serif; font-weight: 700;
    font-size: 118px; letter-spacing: 1px; color: var(--white); line-height: 1;
  }
  .front-services {
    position: absolute; left: 278px; top: 284px;
    font-family: "Roboto", sans-serif; font-weight: 400; font-size: 19px; color: var(--teal);
    letter-spacing: 1px;
  }

  /* Back */
  .card-back { top: 553px; background: var(--paper); }
  .back-identity {
    position: absolute; left: 56px; top: 56px;
    display: flex; align-items: center; gap: 20px;
  }
  .back-mark { width: 90px; height: 90px; border-radius: 50%; background: var(--blue-brand); }
  .back-name {
    font-family: "Roboto Condensed", sans-serif; font-weight: 700;
    font-size: 52px; color: var(--grey-brand); letter-spacing: 1px; line-height: 1;
  }
  .person { position: absolute; left: 56px; top: 178px; }
  .person-name {
    font-family: "Roboto", sans-serif; font-weight: 700; font-size: 30px; color: var(--blue-brand);
  }
  .person-role {
    font-family: "Roboto", sans-serif; font-weight: 500; font-size: 16px; color: var(--ink); margin-top: 4px;
  }
  .divider {
    position: absolute; left: 380px; top: 60px; width: 1.5px; height: 250px; background: var(--rule);
  }
  .contacts {
    position: absolute; left: 410px; top: 92px; list-style: none;
    font-family: "Roboto", sans-serif; font-weight: 400; font-size: 18px; color: var(--ink);
  }
  .contacts li { display: flex; align-items: center; gap: 12px; margin-bottom: 16px; white-space: nowrap; }
  .contacts svg { width: 18px; height: 18px; flex: none; }
  .socials {
    position: absolute; right: 48px; bottom: 36px; display: flex; gap: 16px;
  }
  .social-dot { width: 28px; height: 28px; border-radius: 50%; background: var(--social); }
</style>
</head>
<body>
<main class="canvas">
  <section class="card card-front" aria-label="Card front">
    <div class="front-lockup">
      <div class="front-mark"></div>
      <div class="front-name">KIVORA</div>
    </div>
    <p class="front-services">EFTPOS | ONLINE | MOBILE</p>
  </section>

  <section class="card card-back" aria-label="Card back">
    <div class="back-identity">
      <div class="back-mark"></div>
      <div class="back-name">KIVORA</div>
    </div>
    <div class="person">
      <p class="person-name">Your Name</p>
      <p class="person-role">Business Owner</p>
    </div>
    <div class="divider"></div>
    <ul class="contacts">
      <li>
        <svg viewBox="0 0 20 20" fill="none" stroke="#1e2a33" stroke-width="1.5"><rect x="5.5" y="1.5" width="9" height="17" rx="1.8"/><path d="M8.5 15.5h3"/></svg>
        <span>0455 806 274</span>
      </li>
      <li>
        <svg viewBox="0 0 20 20" fill="none" stroke="#1e2a33" stroke-width="1.5"><circle cx="10" cy="10" r="8.5"/><path d="M7 6.5c0 4 2.5 7 6 7l.6-1.6-1.8-1-1 .8c-1.2-.6-2-1.6-2.4-2.8l.8-1-1-1.8z" fill="#1e2a33" stroke="none"/></svg>
        <span>02 7391 5082</span>
      </li>
      <li>
        <svg viewBox="0 0 20 20" fill="none" stroke="#1e2a33" stroke-width="1.5"><rect x="2" y="4.5" width="16" height="11"/><path d="M2 4.5l8 6.5 8-6.5M2 15.5l6-5M18 15.5l-6-5"/></svg>
        <span>contact@kivora.com.au</span>
      </li>
      <li>
        <svg viewBox="0 0 20 20" fill="none" stroke="#1e2a33" stroke-width="1.3"><circle cx="10" cy="10" r="8.5"/><ellipse cx="10" cy="10" rx="3.8" ry="8.5"/><path d="M1.5 10h17M3 5.5h14M3 14.5h14"/></svg>
        <span>kivora.com.au</span>
      </li>
    </ul>
    <div class="socials">
      <span class="social-dot"></span>
      <span class="social-dot"></span>
      <span class="social-dot"></span>
    </div>
  </section>
</main>
</body>
</html>
```